Small business that sells dolls used in the investigation of sudden infant deaths needs a website de

We need a modern update to our very simple current website. We are a small business that manufactures and sells featureless dolls used in the training and investigation of sudden infant deaths. With our customer base being primarily government organizations we are looking for design that is to the point and functional while also being engaging.
Updates

Target Market(s)

Our target audience are organizations such as government offices and training organizations looking for information about our product. This makes readability and ease-of-use of the design very important.

Number of Pages Required

5+ page

Font styles to use
Serif

Colors

Designer to choose colors to be used in the design.

Requirements
Must have
• Straightforward website focused towards the product being sold. With secondary focus is being how to contact the business and the care and use of the product. The business logo is orange and blue, these colors do not necessarily need to show up in the website design. Darker and muted/contrasting colors would probably be better.
Nice to have
• It would be nice if the website had a professional feel, that is slightly maternal but is not cutesy. Given the nature of our product, we also would like a site that is very respectful for any case that our product might be used in it.

```html
<!DOCTYPE html>
<html lang="en">
<head>
<meta charset="utf-8">
<title>Quiet Harbor SUIDI Dolls — Order</title>
<link rel="stylesheet" href="https://fonts.googleapis.com/css2?family=Poppins:wght@400;500;600;700;800&family=Roboto+Slab:wght@600;700&family=Source+Sans+3:wght@400;600&display=swap">
<style>
:root{
  --orange:#e8441c;
  --blue:#3b97e3;
  --ink:#111111;
  --text:#333333;
  --muted:#555555;
  --cream:#f4f0f0;
  --footer:#0c151d;
  --white:#ffffff;
  --line:#cfcfcf;
}
*{box-sizing:border-box;margin:0;padding:0}
html,body{width:1200px;height:3488px;overflow:hidden}
body{position:relative;background:var(--white);font-family:"Source Sans 3",sans-serif;color:var(--text)}
.abs{position:absolute}

/* header */
.hero{left:0;top:0;width:1200px;height:553px;background:linear-gradient(180deg,#2a2426 0%,#5a2a30 30%,#b8434f 60%,#9a3040 85%,#3a2226 100%)}
.brand-dot{left:35px;top:23px;width:104px;height:104px;border-radius:50%;background:var(--blue)}
.brand-name{left:153px;top:42px;font-family:"Roboto Slab",serif;font-weight:700;font-size:29px;color:var(--white)}
.brand-tag{left:155px;top:82px;font-family:"Source Sans 3",sans-serif;font-weight:600;font-size:12.5px;color:var(--white)}
.call{left:942px;top:21px;width:214px;height:44px;background:var(--white);border:2px solid var(--blue);display:flex;align-items:center}
.call-icon{width:42px;height:40px;background:var(--blue);display:flex;align-items:center;justify-content:center}
.call-num{flex:1;text-align:center;font-family:"Poppins",sans-serif;font-weight:700;font-size:20px;color:var(--orange)}
.nav{left:600px;top:78px;display:flex;gap:0;font-family:"Poppins",sans-serif;font-weight:600;font-size:13.5px;color:var(--white)}
.nav a{color:var(--white);text-decoration:none;padding:4px 8px;margin-right:10px}
.nav a.active{background:var(--orange)}

/* products features */
.h2{width:1200px;text-align:center;font-family:"Poppins",sans-serif;font-weight:800;color:var(--ink)}
.rule{left:582px;top:668px;width:36px;height:2px;background:#999}
.feat{width:240px;text-align:center}
.feat h3{font-family:"Poppins",sans-serif;font-weight:800;font-size:14px;color:var(--ink);margin-bottom:12px}
.feat p{font-size:15px;line-height:19px;color:#333}
.emblem{left:495px;top:809px;width:210px;height:210px;border-radius:50%;border:14px solid var(--blue);display:flex;align-items:center;justify-content:center;text-align:center;font-family:"Roboto Slab",serif;font-weight:700;font-size:18px;color:var(--blue);padding:20px}

/* order */
.order{left:0;top:1163px;width:1200px;height:1826px;background:var(--cream)}
.kicker{top:1223px;width:1200px;text-align:center;font-family:"Poppins",sans-serif;font-weight:600;font-size:18px;color:var(--ink)}
.product-photo{border-radius:50%}
.p-title{font-family:"Poppins",sans-serif;font-weight:700;font-size:19px;color:var(--ink)}
.p-title span{color:var(--orange)}
.price-box{width:305px;height:104px;background:var(--white);border:1px solid var(--line);display:flex;flex-direction:column;justify-content:center;padding-left:52px;gap:8px;font-family:"Poppins",sans-serif;font-weight:700;font-size:13px;color:var(--ink)}
.price-box b{color:var(--orange);font-weight:700}
.select{width:305px;height:40px;background:var(--white);border:1px solid var(--line);display:flex;align-items:center;justify-content:space-between;padding:0 18px;font-family:"Poppins",sans-serif;font-weight:700;font-size:11.5px;color:var(--ink)}
.ship h4{font-family:"Poppins",sans-serif;font-weight:600;font-size:20px;color:var(--ink);margin-bottom:14px}
.ship p{font-size:18px;color:#555;margin-bottom:14px}
.cart{width:163px;height:48px;background:var(--orange);color:var(--white);display:flex;align-items:center;justify-content:center;font-family:"Poppins",sans-serif;font-weight:700;font-size:15px;letter-spacing:1.5px}
.bag-price{font-family:"Poppins",sans-serif;font-weight:700;font-size:29px;color:var(--orange)}

/* footer */
.footer{left:0;top:2989px;width:1200px;height:499px;background:var(--footer)}
.band{left:128px;top:2945px;width:930px;height:88px;background:var(--orange);display:flex;align-items:center;padding-left:26px}
.band-q{font-family:"Poppins",sans-serif;font-weight:700;font-size:13px;line-height:14px;color:var(--white);margin-left:18px}
.band-num{font-family:"Poppins",sans-serif;font-weight:700;font-size:33px;color:var(--white);margin-left:14px}
.email{margin-left:56px;width:253px;height:30px;border-radius:15px;background:var(--white);display:flex;align-items:center;padding-left:14px;gap:12px;font-size:12px;font-style:italic;color:#666}
.subscribe{margin-left:16px;width:124px;height:30px;border-radius:15px;background:var(--blue);color:var(--white);display:flex;align-items:center;justify-content:center;font-family:"Poppins",sans-serif;font-weight:600;font-size:13px}
.foot-mark{left:153px;top:3109px;width:220px;height:220px;border-radius:50%;background:var(--white);display:flex;align-items:center;justify-content:center;text-align:center;font-family:"Roboto Slab",serif;font-weight:700;font-size:22px;color:var(--footer);padding:28px}
.col h5{font-family:"Poppins",sans-serif;font-weight:600;font-size:13px;color:var(--white);letter-spacing:.5px;margin-bottom:22px}
.col li{list-style:none;font-family:"Poppins",sans-serif;font-size:12.5px;color:#d9dde2;height:29px;display:flex;align-items:center;gap:12px}
.col li i{width:10px;height:10px;border-radius:50%;background:#d9dde2;display:inline-block}
.follow li{height:44px}
.contact-item{display:flex;gap:14px;margin-bottom:22px;padding-bottom:16px;border-bottom:1px solid #2b3540;width:210px}
.contact-item svg{flex:none}
.contact-item .lbl{font-family:"Poppins",sans-serif;font-size:12px;color:var(--orange)}
.contact-item .val{font-family:"Poppins",sans-serif;font-size:12px;line-height:14px;color:#d9dde2}
.divider{left:112px;top:3419px;width:960px;height:1px;background:#4a545e}
.copy{top:3444px;width:1200px;text-align:center;font-family:"Poppins",sans-serif;font-size:11.5px;color:#cfd4d9}
</style>
</head>
<body>

<header>
  <div class="abs hero" role="img" aria-label="Photo of rows of red investigation dolls laid out on a table"></div>
  <div class="abs brand-dot"></div>
  <div class="abs brand-name">Quiet Harbor SUIDI Dolls</div>
  <div class="abs brand-tag">Investigation Dolls for Sudden, Unexplained Infant Death</div>
  <div class="abs call">
    <div class="call-icon">
      <svg width="20" height="20" viewBox="0 0 24 24"><path fill="#fff" d="M6.6 10.8c1.4 2.8 3.8 5.1 6.6 6.6l2.2-2.2c.3-.3.7-.4 1-.2 1.1.4 2.3.6 3.6.6.6 0 1 .4 1 1V20c0 .6-.4 1-1 1C10.6 21 3 13.4 3 4c0-.6.4-1 1-1h3.5c.6 0 1 .4 1 1 0 1.3.2 2.5.6 3.6.1.3 0 .7-.2 1z"/></svg>
    </div>
    <div class="call-num">(555) 214-3380</div>
  </div>
  <nav class="abs nav">
    <a>HOME</a><a>ABOUT US</a><a class="active">ORDER</a><a>CARE AND USE OF DOLLS</a><a>CONTACT</a>
  </nav>
</header>

<section class="products">
  <h2 class="abs h2" style="top:612px;font-size:33px">PRODUCTS</h2>
  <div class="abs rule"></div>

  <svg class="abs" style="left:0;top:0" width="1200" height="1100" viewBox="0 0 1200 1100">
    <g fill="none" stroke="#555" stroke-width="1.5">
      <polyline points="360,786 477,786 477,835"/>
      <polyline points="840,786 726,786 726,835"/>
      <polyline points="360,1044 477,1044 477,993"/>
      <polyline points="840,1044 726,1044 726,993"/>
    </g>
    <g fill="#e8441c">
      <circle cx="477" cy="835" r="7"/>
      <circle cx="726" cy="835" r="7"/>
      <circle cx="477" cy="993" r="7"/>
      <circle cx="726" cy="993" r="7"/>
    </g>
  </svg>

  <div class="abs emblem">Quiet Harbor</div>

  <div class="abs feat" style="left:115px;top:731px"><h3>SAFETY</h3><p>Lorem ipsum dolor sit amet, consectetur adipiscing elit, sed do eiusmod tempor incididunt.</p></div>
  <div class="abs feat" style="left:855px;top:731px"><h3>WATER REPELLENTS</h3><p>Lorem ipsum dolor sit amet, consectetur adipiscing elit, sed do eiusmod tempor incididunt.</p></div>
  <div class="abs feat" style="left:115px;top:996px"><h3>GOOD SHAPE</h3><p>Lorem ipsum dolor sit amet, consectetur adipiscing elit, sed do eiusmod tempor incididunt.</p></div>
  <div class="abs feat" style="left:855px;top:996px"><h3>LIGHT COLORED</h3><p>Lorem ipsum dolor sit amet, consectetur adipiscing elit, sed do eiusmod tempor incididunt.</p></div>
</section>

<section>
  <div class="abs order"></div>
  <div class="abs kicker">BUY NOW</div>
  <h2 class="abs h2" style="top:1253px;font-size:33px;font-weight:600">ORDER INFORMATION</h2>

  <!-- white dolls -->
  <div class="abs product-photo" style="left:210px;top:1390px;width:390px;height:390px;background:#e6e1e1"></div>
  <div class="abs product-photo" style="left:198px;top:1380px;width:380px;height:380px;background:radial-gradient(circle at 50% 45%,#d9d9d9 0%,#8a8a8a 22%,#0a0a0a 42%,#000 100%)" role="img" aria-label="Photo of a white featureless investigation doll"></div>
  <div class="abs p-title" style="left:675px;top:1380px">SUIDI DOLLS (WHITE)</div>
  <div class="abs price-box" style="left:675px;top:1424px"><div>6 LB. DOLLS:&nbsp; WHITE &nbsp; $39.00</div><div>8 LB. DOLLS:&nbsp; WHITE &nbsp; $40.00</div></div>
  <div class="abs select" style="left:675px;top:1551px"><span>SELECT WEIGHT</span><svg width="12" height="8"><path d="M0 0h12L6 7z" fill="#111"/></svg></div>
  <div class="abs ship" style="left:679px;top:1618px"><h4>Shipping &amp; handling:</h4><p>1 - 2 dolls: $13.60</p><p>3 dolls: $18.85</p></div>
  <div class="abs cart" style="left:682px;top:1745px">ADD TO CART</div>

  <!-- orange dolls -->
  <div class="abs product-photo" style="left:210px;top:1925px;width:390px;height:390px;background:var(--orange)"></div>
  <div class="abs product-photo" style="left:198px;top:1915px;width:380px;height:380px;background:radial-gradient(circle at 50% 45%,#f04a1e 0%,#d94a2a 22%,#a9a9a9 40%,#b0b0b0 100%)" role="img" aria-label="Photo of an orange featureless investigation doll"></div>
  <div class="abs p-title" style="left:675px;top:1915px">SUIDI DOLLS <span>(ORANGE)</span></div>
  <div class="abs price-box" style="left:675px;top:1959px"><div>6 LB. DOLLS:&nbsp; <b>ORANGE &nbsp; $41.00</b></div><div>8 LB. DOLLS:&nbsp; <b>ORANGE &nbsp; $42.00</b></div></div>
  <div class="abs select" style="left:675px;top:2086px"><span>SELECT WEIGHT</span><svg width="12" height="8"><path d="M0 0h12L6 7z" fill="#111"/></svg></div>
  <div class="abs ship" style="left:679px;top:2153px"><h4>Shipping &amp; handling:</h4><p>1 - 2 dolls: $13.60</p><p>3 dolls: $18.85</p></div>
  <div class="abs cart" style="left:682px;top:2280px">ADD TO CART</div>

  <!-- duffel bags -->
  <div class="abs product-photo" style="left:210px;top:2481px;width:390px;height:390px;background:#dcd6d6"></div>
  <div class="abs product-photo" style="left:198px;top:2467px;width:380px;height:380px;background:radial-gradient(circle at 50% 50%,#1a1a1a 0%,#2a2a2a 25%,#ffffff 42%,#ffffff 100%)" role="img" aria-label="Photo of a black duffel bag"></div>
  <div class="abs p-title" style="left:675px;top:2470px">BLACK DUFFEL BAGS</div>
  <div class="abs bag-price" style="left:679px;top:2502px">$21.00</div>
  <div class="abs select" style="left:675px;top:2581px"><span>SELECT QTY</span><svg width="12" height="8"><path d="M0 0h12L6 7z" fill="#111"/></svg></div>
  <div class="abs ship" style="left:679px;top:2646px"><h4>Shipping &amp; handling:</h4><p>1 - 2 dolls: $13.60</p><p>3 dolls: $18.85</p></div>
  <div class="abs cart" style="left:682px;top:2775px">ADD TO CART</div>
</section>

<footer>
  <div class="abs footer"></div>
  <div class="abs band">
    <svg width="34" height="34" viewBox="0 0 24 24"><path fill="#fff" d="M6.6 10.8c1.4 2.8 3.8 5.1 6.6 6.6l2.2-2.2c.3-.3.7-.4 1-.2 1.1.4 2.3.6 3.6.6.6 0 1 .4 1 1V20c0 .6-.4 1-1 1C10.6 21 3 13.4 3 4c0-.6.4-1 1-1h3.5c.6 0 1 .4 1 1 0 1.3.2 2.5.6 3.6.1.3 0 .7-.2 1z"/></svg>
    <div class="band-q">DO YOU HAVE<br>A QUESTION?</div>
    <div class="band-num">+0123 456 789</div>
    <div class="email">
      <svg width="12" height="9" viewBox="0 0 12 9"><rect width="12" height="9" fill="#888"/><path d="M0 0l6 5 6-5" stroke="#fff" fill="none"/></svg>
      Enter your email address
    </div>
    <div class="subscribe">Subscribe</div>
  </div>

  <div class="abs foot-mark">Quiet Harbor</div>

  <div class="abs col" style="left:470px;top:3114px">
    <h5>QUICK LINKS</h5>
    <ul><li><i></i>Home</li><li><i></i>About</li><li><i></i>Products</li><li><i></i>Features</li><li><i></i>Testimonials</li><li><i></i>Contact</li></ul>
  </div>
  <div class="abs col follow" style="left:677px;top:3114px">
    <h5>FOLLOW US</h5>
    <ul><li>Community</li><li>Gallery</li><li>Updates</li><li>Network</li></ul>
  </div>
  <div class="abs col" style="left:847px;top:3114px">
    <h5>CONTACT US</h5>
    <div class="contact-item">
      <svg width="26" height="26" viewBox="0 0 26 26"><circle cx="13" cy="13" r="13" fill="#e8441c"/><path d="M13 6a4.5 4.5 0 0 0-4.5 4.5C8.5 14 13 19 13 19s4.5-5 4.5-8.5A4.5 4.5 0 0 0 13 6zm0 6.2a1.7 1.7 0 1 1 0-3.4 1.7 1.7 0 0 1 0 3.4z" fill="#fff"/></svg>
      <div><div class="lbl">Head Office</div><div class="val">123, Main Street, Your City<br>USA 789456</div></div>
    </div>
    <div class="contact-item">
      <svg width="26" height="26" viewBox="0 0 26 26"><circle cx="13" cy="13" r="13" fill="#e8441c"/><path d="M10 11.5c.8 1.6 2.2 3 3.8 3.8l1.3-1.3c.2-.2.4-.2.6-.1.6.2 1.3.3 2 .3.3 0 .6.2.6.6V17c0 .3-.3.6-.6.6C12.5 17.6 8.4 13.5 8.4 8.4c0-.3.3-.6.6-.6h2c.4 0 .6.3.6.6 0 .7.1 1.4.3 2 .1.2 0 .4-.1.6z" fill="#fff"/></svg>
      <div><div class="lbl">Phone Number</div><div class="val">+123 456 7890<br>+123 456 7890</div></div>
    </div>
    <div class="contact-item" style="border-bottom:none">
      <svg width="26" height="26" viewBox="0 0 26 26"><circle cx="13" cy="13" r="13" fill="#e8441c"/><rect x="7.5" y="9" width="11" height="8" fill="#fff"/><path d="M7.5 9l5.5 4.5L18.5 9" stroke="#e8441c" fill="none"/></svg>
      <div><div class="lbl">Email</div><div class="val">info@quietharbordolls.com<br>www.quietharbordolls.com</div></div>
    </div>
  </div>

  <div class="abs divider"></div>
  <div class="abs copy">Copyright © 2019. All Rights Reserved.</div>
</footer>

</body>
</html>
```